Poster of Core Values & Motto

Create our core values poster and motto. Attached are our core values and our Motto. This poster represents both of our companies Tidy Pulp & CuraBinix.

Target Market(s)

Our team / employees

Industry/Entity Type

Shredding and Medical Waste

Colors
59FF00
82FF00
B8FF75
E3FFCB
F4FFEA
EB3D1F
EC4F4E
F09395
F8D3D4
FCEDEE

Requirements
Must have
• Include both companies logos

```html
<!DOCTYPE html>
<html lang="en">
<head>
<meta charset="UTF-8">
<title>Our Values Poster</title>
<link rel="stylesheet" href="https://fonts.googleapis.com/css2?family=Barlow:wght@700;800&family=Figtree:wght@400;500&display=swap">
<style>
  :root {
    --bg: #e4e5e5;
    --paper: #ffffff;
    --red: #d42027;
    --red-deep: #6c0f14;
    --red-mid: #8e1a1f;
    --green: #00a24a;
    --ink: #2b2b2b;
  }
  * { margin: 0; padding: 0; box-sizing: border-box; }
  html, body { width: 1200px; height: 1179px; overflow: hidden; background: var(--bg); }
  .poster {
    position: absolute; left: 220px; top: 20px;
    width: 760px; height: 1140px;
    background: var(--paper);
    overflow: hidden;
    box-shadow: 0 6px 18px rgba(0,0,0,0.12);
  }
  .title {
    position: absolute; top: 34px; left: 0; width: 100%;
    text-align: center;
    font-family: "Barlow", sans-serif; font-weight: 800;
    font-size: 87px; line-height: 1; letter-spacing: 0.5px;
  }
  .title .word-our { color: var(--red); }
  .title .word-values { color: var(--green); }
  .value {
    position: absolute; left: 139px;
    display: flex; align-items: center;
  }
  .value-icon {
    width: 53px; height: 53px; flex: none;
    border: 1.5px solid var(--green); border-radius: 50%;
    display: flex; align-items: center; justify-content: center;
  }
  .value-icon svg { width: 32px; height: 32px; fill: var(--red); }
  .value-text { margin-left: 50px; }
  .value-name {
    font-family: "Barlow", sans-serif; font-weight: 800;
    font-size: 35px; line-height: 1; color: var(--green); letter-spacing: 0.3px;
  }
  .value-desc {
    font-family: "Figtree", sans-serif; font-weight: 400;
    font-size: 14px; line-height: 1.2; color: var(--ink); margin-top: 3px;
  }
  .feature { position: absolute; left: 0; top: 0; width: 760px; height: 1140px; }
  .feature-head { font-family: "Barlow", sans-serif; font-weight: 800; font-size: 112px; fill: #ffffff; }
  .feature-sub { font-family: "Barlow", sans-serif; font-weight: 700; font-size: 39px; fill: #ffffff; }
  .brand-name { font-family: "Barlow", sans-serif; font-weight: 800; font-size: 34px; }
</style>
</head>
<body>
<main class="poster">
  <h1 class="title"><span class="word-our">OUR</span> <span class="word-values">VALUES</span></h1>

  <section class="value" style="top:150px">
    <div class="value-icon"><svg viewBox="0 0 32 32"><circle cx="16" cy="7" r="3.5"/><circle cx="8" cy="9" r="3"/><circle cx="24" cy="9" r="3"/><path d="M11 12h10v10h-2v8h-6v-8h-2z"/><path d="M3 14h8v8H9v6H5v-6H3z"/><path d="M21 14h8v8h-2v6h-4v-6h-2z"/></svg></div>
    <div class="value-text"><h2 class="value-name">SYNERGY / TEAMWORK</h2><p class="value-desc">Get it done attitude with humble confidence</p></div>
  </section>

  <section class="value" style="top:226px">
    <div class="value-icon"><svg viewBox="0 0 32 32"><path d="M2 9h19v15H2z"/><path d="M21 13h6l4 5v6H21z"/><circle cx="8" cy="25" r="3" fill="#fff"/><circle cx="8" cy="25" r="2"/><circle cx="25" cy="25" r="3" fill="#fff"/><circle cx="25" cy="25" r="2"/><text x="11.5" y="19" font-size="9" font-family="Figtree, sans-serif" fill="#fff" text-anchor="middle">$</text></svg></div>
    <div class="value-text"><h2 class="value-name">SAFE AND SECURE</h2><p class="value-desc">We are just as secure as an armored truck with money</p></div>
  </section>

  <section class="value" style="top:313px">
    <div class="value-icon"><svg viewBox="0 0 32 32"><circle cx="12" cy="8" r="5"/><path d="M2 27c0-7 4-11 10-11 2 0 4 .5 5 1.5V27z"/><path d="M23 15l7 3v5c0 4-3 7-7 8-4-1-7-4-7-8v-5z"/><path d="M19.5 22.5l2.5 2.5 4.5-5" stroke="#fff" stroke-width="1.8" fill="none"/></svg></div>
    <div class="value-text"><h2 class="value-name">HONESTY / INTEGRITY</h2><p class="value-desc">Do the right thing</p></div>
  </section>

  <section class="value" style="top:402px">
    <div class="value-icon"><svg viewBox="0 0 32 32"><path d="M3 5h16v4c0 5-3 8-8 8S3 14 3 9z"/><path d="M9 17h4v5H9z"/><path d="M6 22h10v3H6zM4 26h14v3H4z"/><circle cx="25" cy="6" r="3"/><path d="M21 10h8v10h-2v9h-4v-9h-2z"/></svg></div>
    <div class="value-text"><h2 class="value-name">EXCELLENCE</h2><p class="value-desc">Exceed expectations with a smile</p></div>
  </section>

  <section class="value" style="top:495px">
    <div class="value-icon"><svg viewBox="0 0 32 32"><path d="M4 24h4v6H4zM11 20h4v10h-4zM18 15h4v15h-4zM25 9h4v21h-4z"/><path d="M16 2l3 1-4 7-3-2z"/><path d="M8 12l4-4 2 2-4 4z"/></svg></div>
    <div class="value-text"><h2 class="value-name">EFFICIENT</h2><p class="value-desc">On-time, sense of urgency, always trying to improve</p></div>
  </section>

  <section class="value" style="top:587px">
    <div class="value-icon"><svg viewBox="0 0 32 32"><circle cx="12" cy="9" r="5"/><path d="M2 30c0-8 4-12 10-12 2 0 4 .5 5 1.5V30z"/><path d="M23 13l7 3v5c0 5-3 8-7 9-4-1-7-4-7-9v-5z"/></svg></div>
    <div class="value-text"><h2 class="value-name">DEPENDABLE</h2><p class="value-desc">Do what you say you will do</p></div>
  </section>

  <svg class="feature" viewBox="0 0 1149 1723" preserveAspectRatio="none">
    <defs>
      <linearGradient id="panelTone" x1="0" y1="0" x2="1" y2="0">
        <stop offset="0" stop-color="#6c0f14"/>
        <stop offset="0.6" stop-color="#74121a"/>
        <stop offset="1" stop-color="#9a2128"/>
      </linearGradient>
    </defs>
    <path fill="var(--green)" d="M0,1245 L470,1137 Q490,1132 489,1112 L487,1078 Q486,1050 512,1044 L1015,930 Q1055,922 1066,960 L1149,1250 L1149,1400 L640,1620 Q600,1640 590,1723 L0,1723 Z"/>
    <path role="img" aria-label="Photo of a staff member reading a phone beside scattered red tiles showing the value icons" fill="url(#panelTone)" transform="translate(12,14)" d="M0,1245 L470,1137 Q490,1132 489,1112 L487,1078 Q486,1050 512,1044 L1015,930 Q1055,922 1066,960 L1149,1250 L1149,1420 L665,1632 Q625,1652 610,1709 L0,1709 Z"/>
    <g transform="rotate(-12.5 556 1225)">
      <text class="feature-head" x="556" y="1225">PURPOSE/</text>
      <text class="feature-head" x="556" y="1318">CAUSE/</text>
      <text class="feature-head" x="556" y="1411">PASSION</text>
      <text class="feature-sub" x="560" y="1463">Remind people what</text>
      <text class="feature-sub" x="560" y="1505">great service looks like.</text>
    </g>
    <text class="brand-name" x="712" y="1680" fill="var(--red)">CuraBinix</text>
    <rect x="930" y="1630" width="2" height="62" fill="#555"/>
    <text class="brand-name" x="952" y="1680" fill="var(--green)">Tidy Pulp</text>
  </svg>
</main>
</body>
</html>
```